Trade Show booth design

I need the following designs for my trade booth:
1. backboard design 3m Wx2mH
2. Tressle table, tablecloth front panel design 1800W x 740mmH
3. Pop-up banner. I have included our logos and some design content ideas:
Headline:
"Cleaner Classrooms. Safer Schools."
Subheadline:
"Specialist Cleaning Solutions for Education Facilities"
Key Points to Grab Attention:
Healthy Environments: Create hygienic, safe learning spaces for students and staff with our expert cleaning services.
Tailored to Your Needs: Custom cleaning plans for classrooms, labs, libraries, and sports facilities.
Affordable Excellence: Premium results without premium costs – tailored plans mean you only pay for what you need.
Safety First: All staff are trained, highly vetted, and hold current Working with Children Checks (WWCC).
Eco-Conscious Cleaning: Using non-toxic, eco-friendly products certified for health and safety.
What Schools Really Need:
Reliability: Consistent, high-quality cleaning from a trusted provider.
Cost-Effectiveness: Solutions that fit tight budgets while maintaining high standards.
Expertise: Over 30 years of experience in education facility cleaning.
Disinfection Services: Focus on high-touch areas to reduce the spread of germs and ensure peace of mind.
Visual Elements:
Images of bright, clean classrooms, a happy teacher welcoming students, or students collaborating in a spotless library.
Icons representing safety (shield), hygiene (sparkling star), and eco-friendliness (leaf).
Your logo with the tagline: "Trusted by Queensland Schools Since 1995."
Call-to-Action:
"Visit us to discuss your school’s cleaning needs and book a FREE consultation."
Include contact details: Phone: 1300 649 315 | Website: www.duravoss.com.au
Target Market(s)
Education sector
Industry/Entity Type
Commercial Cleaning
Font styles to use
Other font styles liked:
- Montserrat
Look and feel

```html
<!DOCTYPE html>
<html lang="en">
<head>
<meta charset="utf-8">
<title>Duravoss Facility Cleaning – Education Backboard</title>
<link rel="stylesheet" href="https://fonts.googleapis.com/css2?family=Montserrat:wght@400;500;700;800&display=swap">
<style>
  :root {
    --navy: #1a3d5f;
    --navy-deep: #163654;
    --ink: #1e1e1e;
    --backdrop: #cde0fb;
    --paper: #ffffff;
    --silver: #c9ccd1;
    --silver-light: #eceef1;
    --ring: #e9ebee;
  }
  * { box-sizing: border-box; margin: 0; padding: 0; }
  html, body { width: 1200px; height: 600px; overflow: hidden; }
  body {
    background: var(--backdrop);
    font-family: "Montserrat", Arial, sans-serif;
    position: relative;
  }
  .board {
    position: absolute;
    left: 183px; top: 22px;
    width: 833px; height: 556px;
    background: var(--paper);
    overflow: hidden;
    box-shadow: 0 2px 6px rgba(20,40,70,.18);
  }
  .classroom-photo {
    position: absolute;
    left: 0; top: 250px; width: 833px; height: 306px;
    background: linear-gradient(180deg, rgba(255,255,255,1) 0%, #e4e8ec 35%, #d3d7dc 65%, #e9ebee 100%);
  }
  .waves { position: absolute; left: 0; top: 0; width: 833px; height: 556px; }
  .brand {
    position: absolute; left: 0; right: 0; top: 40px;
    display: flex; justify-content: center; align-items: center; gap: 10px;
  }
  .brand-dot { width: 26px; height: 26px; border-radius: 50%; background: var(--navy); }
  .brand-name {
    font-weight: 800; font-size: 30px; color: var(--navy); letter-spacing: 1px;
  }
  .headline {
    position: absolute; left: 0; right: 0; top: 100px;
    text-align: center; color: var(--navy);
    font-weight: 800; font-size: 38px; line-height: 38px; letter-spacing: .3px;
  }
  .subline-pill {
    position: absolute; left: 77px; top: 183px; width: 678px; height: 25px;
    background: linear-gradient(90deg, var(--silver) 0%, var(--silver-light) 20%, var(--silver-light) 80%, var(--silver) 100%);
    border-radius: 14px 4px 14px 4px;
  }
  .subline {
    position: absolute; left: 0; right: 0; top: 183px;
    text-align: center; color: var(--navy);
    font-size: 19px; line-height: 25px; font-weight: 500;
  }
  .feature {
    position: absolute; top: 221px; width: 220px;
    text-align: center; color: var(--ink);
    font-size: 16px; line-height: 19.5px;
  }
  .feature b { font-weight: 800; }
  .feature-badge {
    width: 80px; height: 80px; margin: 0 auto 10px;
    border-radius: 50%; background: var(--ring);
    display: flex; align-items: center; justify-content: center;
  }
  .feature-badge svg { width: 68px; height: 68px; }
  .feature--expertise { left: 72px; }
  .feature--trust { left: 306px; }
  .feature--eco { left: 540px; }
  .cta {
    position: absolute; right: 32px; top: 469px;
    text-align: right; color: #fff;
    font-size: 14px; line-height: 16.5px;
  }
  .contact {
    position: absolute; right: 32px; top: 505px;
    display: flex; align-items: center; gap: 4px;
    color: #fff; font-size: 19px; line-height: 22px; white-space: nowrap;
  }
  .contact svg { width: 14px; height: 16px; }
</style>
</head>
<body>
  <main class="board">
    <div class="classroom-photo" role="img" aria-label="Bright empty classroom with rows of white desks and chairs"></div>

    <svg class="waves" viewBox="0 0 833 556" aria-hidden="true">
      <defs>
        <linearGradient id="silverSweep" x1="0" y1="0" x2="1" y2="0">
          <stop offset="0" stop-color="#f4f5f7"/>
          <stop offset=".5" stop-color="#cfd2d6"/>
          <stop offset="1" stop-color="#e8eaed"/>
        </linearGradient>
      </defs>
      <path d="M0,380 C70,470 170,545 300,530 C430,515 520,440 640,420 C730,405 800,430 833,440 L833,556 L0,556 Z" fill="url(#silverSweep)"/>
      <path d="M0,437 C70,500 160,550 280,550 C400,550 480,490 600,458 C700,432 780,445 833,480 L833,556 L0,556 Z" fill="var(--navy-deep)"/>
    </svg>

    <header class="brand">
      <span class="brand-dot"></span>
      <span class="brand-name">DURAVOSS</span>
    </header>

    <h1 class="headline">CREATING CLEANER,<br>SAFER LEARNING ENVIRONMENTS</h1>
    <div class="subline-pill"></div>
    <p class="subline">Specialists in Education Facility Cleaning &amp; Eco-Friendly Services</p>

    <section class="feature feature--expertise">
      <div class="feature-badge">
        <svg viewBox="0 0 68 68" aria-hidden="true">
          <circle cx="34" cy="34" r="34" fill="var(--navy)"/>
          <circle cx="34" cy="34" r="30" fill="none" stroke="#fff" stroke-width=".8" stroke-dasharray="2 2"/>
          <circle cx="34" cy="24" r="7" fill="none" stroke="#fff" stroke-width="1.6"/>
          <path d="M30.5,24 l2.5,2.5 l4.5,-5" fill="none" stroke="#fff" stroke-width="1.6"/>
          <path d="M18,38 l10,-6 l12,0 l10,6 M26,40 l8,8 l8,-8" fill="none" stroke="#fff" stroke-width="1.6" stroke-linejoin="round"/>
        </svg>
      </div>
      Over <b>30 years</b><br>of expertise in<br>commercial cleaning.
    </section>

    <section class="feature feature--trust">
      <div class="feature-badge">
        <svg viewBox="0 0 68 68" aria-hidden="true">
          <circle cx="34" cy="34" r="34" fill="var(--navy)"/>
          <circle cx="34" cy="34" r="30" fill="none" stroke="#fff" stroke-width=".8" stroke-dasharray="2 2"/>
          <path d="M22,17 l1.5,3 l3,.3 l-2.3,2 l.7,3 l-2.9,-1.6 l-2.9,1.6 l.7,-3 l-2.3,-2 l3,-.3 Z M34,14 l1.5,3 l3,.3 l-2.3,2 l.7,3 l-2.9,-1.6 l-2.9,1.6 l.7,-3 l-2.3,-2 l3,-.3 Z M46,17 l1.5,3 l3,.3 l-2.3,2 l.7,3 l-2.9,-1.6 l-2.9,1.6 l.7,-3 l-2.3,-2 l3,-.3 Z" fill="none" stroke="#fff" stroke-width="1"/>
          <path d="M24,52 l0,-8 q0,-6 10,-6 q10,0 10,6 l0,8 Z" fill="none" stroke="#fff" stroke-width="1.6"/>
        </svg>
      </div>
      Trusted by <b>schools,<br>universities, and TAFEs</b><br>across Queensland.
    </section>

    <section class="feature feature--eco">
      <div class="feature-badge">
        <svg viewBox="0 0 68 68" aria-hidden="true">
          <circle cx="34" cy="34" r="34" fill="var(--navy)"/>
          <circle cx="34" cy="34" r="30" fill="none" stroke="#fff" stroke-width=".8" stroke-dasharray="2 2"/>
          <path d="M16,46 C22,28 40,18 52,22 C54,38 40,50 22,48 Z" fill="#fff"/>
          <path d="M20,46 C30,40 40,32 48,26" fill="none" stroke="var(--navy)" stroke-width="1.6"/>
        </svg>
      </div>
      <b>100% Carbon Neutral<br>and Eco-Certified</b><br>Services.
    </section>

    <p class="cta">Visit us to discuss your school’s cleaning needs<br>and book a FREE consultation.</p>
    <p class="contact">
      <svg viewBox="0 0 14 16" aria-hidden="true"><rect x="3" y="1" width="8" height="14" rx="1.5" fill="none" stroke="#fff" stroke-width="1.3"/><line x1="6" y1="13" x2="8" y2="13" stroke="#fff" stroke-width="1.2"/></svg>
      <span>1300 649 315 |</span>
      <svg viewBox="0 0 16 16" aria-hidden="true"><circle cx="8" cy="8" r="6.5" fill="none" stroke="#fff" stroke-width="1.2"/><ellipse cx="8" cy="8" rx="3" ry="6.5" fill="none" stroke="#fff" stroke-width="1"/><line x1="1.5" y1="8" x2="14.5" y2="8" stroke="#fff" stroke-width="1"/></svg>
      <span>www.duravoss.com.au</span>
    </p>
  </main>
</body>
</html>
```